Aerial photo/video drone company needs new business card

Aerial visual company who offers photos and video services via drones.

We are QVL certified and work in the real estate, insurance, construction, and film industries.

I'm looking for a clean, professional, maybe even edgy design, that will be a conversation starter when networking.

I've included our logo, current business card, and font.

Our current business card is decent; albeit, I'm looking for something more unique. If you folks provide good designs, I'll definitely guarantee payment (and I'm not opposed to tipping if the design is above and beyond).

Target Market(s)

Insurance companies, real estate agents, construction companies, advertising & other creative agencies, and filmmakers/producers.

Industry/Entity Type

Business

Contact Information for Business Card

Company name pronounced air-a-vee.

Font styles to use
Other font styles liked:
• Font was uploaded; that or similar; not opposed to other fonts if they work well with the design

Requirements
Must have
• Clearly prominent logo; my name and title; phone number; email address; web address; mentioned "QVL Certified" or similar; should indicate "Aerial visual"
Nice to have
• Watermark of logo or otherwise
Should not have
• Pictures of drones or scenic shots

```html
<!DOCTYPE html>
<html lang="en">
<head>
<meta charset="utf-8">
<title>altivue business card</title>
<link rel="stylesheet" href="https://fonts.googleapis.com/css2?family=Nunito:wght@500;600;800&display=swap">
<style>
  :root {
    --navy: #253858;
    --blue: #0a9ae0;
    --card-blue: #0e97de;
    --white: #ffffff;
    --ground: #ebebeb;
    --ink-soft: #3f4a5a;
  }
  * { margin: 0; padding: 0; box-sizing: border-box; }
  html, body { width: 1200px; height: 987px; overflow: hidden; }
  body {
    background: var(--ground);
    font-family: "Nunito", sans-serif;
    position: relative;
  }
  .card {
    position: absolute;
    left: 293px;
    width: 615px;
    height: 350px;
    box-shadow: 0 3px 10px rgba(0,0,0,0.25);
    overflow: hidden;
  }
  .card--front { top: 130px; background: var(--white); }
  .card--back { top: 506px; background: var(--card-blue); color: var(--white); text-align: center; }

  .front__tab {
    position: absolute; left: 0; top: 122px;
    width: 12px; height: 47px;
    background: var(--navy);
    clip-path: polygon(0 0, 40% 0, 100% 50%, 40% 100%, 0 100%);
  }
  .front__name {
    position: absolute; left: 37px; top: 126px;
    font-size: 23px; font-weight: 600; color: var(--navy);
  }
  .front__title {
    position: absolute; left: 37px; top: 155px;
    font-size: 16px; font-weight: 500; color: var(--blue);
  }
  .contact {
    position: absolute; left: 37px; top: 187px;
    list-style: none;
  }
  .contact li {
    display: flex; align-items: center; gap: 9px;
    height: 23.5px;
    font-size: 16.5px; color: var(--ink-soft);
  }
  .contact svg { width: 14px; height: 14px; fill: var(--navy); }
  .front__wordmark {
    position: absolute; left: 34px; top: 258px;
    font-size: 74px; font-weight: 800; line-height: 1;
    letter-spacing: 1px; color: var(--navy);
  }
  .front__disc {
    position: absolute; left: 316px; top: 36px;
    width: 282px; height: 282px; border-radius: 50%;
    background: var(--blue);
  }

  .back__disc {
    width: 64px; height: 64px; border-radius: 50%;
    background: var(--white);
    margin: 102px auto 0;
  }
  .back__wordmark {
    font-size: 90px; font-weight: 800; line-height: 1;
    letter-spacing: 2px; margin-top: 2px;
  }
  .back__tagline {
    margin-top: 20px;
    font-size: 17px; font-weight: 500; line-height: 23px;
  }
</style>
</head>
<body>
  <section class="card card--front">
    <div class="front__tab"></div>
    <p class="front__name">Daniel K.Morrow</p>
    <p class="front__title">Owner . sUAS Pilot</p>
    <ul class="contact">
      <li><svg viewBox="0 0 24 24"><path d="M6.6 10.8a15.1 15.1 0 0 0 6.6 6.6l2.2-2.2c.3-.3.7-.4 1-.2 1.1.4 2.3.6 3.6.6.6 0 1 .4 1 1V20c0 .6-.4 1-1 1C10.6 21 3 13.4 3 4c0-.6.4-1 1-1h3.5c.6 0 1 .4 1 1 0 1.3.2 2.5.6 3.6.1.3 0 .7-.2 1z"/></svg>415.302.7788</li>
      <li><svg viewBox="0 0 24 24"><path d="M2 5h20v14H2zM4 7v.4l8 5 8-5V7zm0 2.8V17h16V9.8l-8 5z"/></svg>dan@altivue.com</li>
      <li><svg viewBox="0 0 24 24"><circle cx="12" cy="12" r="10"/><path d="M2 12h20M12 2c3 3 3 17 0 20M12 2c-3 3-3 17 0 20" stroke="#fff" stroke-width="1.5" fill="none"/></svg>www.altivue.com</li>
    </ul>
    <p class="front__wordmark">altivue</p>
    <div class="front__disc"></div>
  </section>

  <section class="card card--back">
    <div class="back__disc"></div>
    <p class="back__wordmark">altivue</p>
    <p class="back__tagline">Aerial Visual for Real Estate • Insurance • Construction • Film<br>QVL Part 107 Commercial sUAS Certified</p>
  </section>
</body>
</html>
```